I need a business card design for a new dance business. I offer classical Indian dance tuition and also professional performances. I want to offer the community a variety of Indian dance experiences which include: group class and private tuition, school and preschool educational courses and workshops. dance theatre performances, community function workshops and performances, Kids Bollywood parties, wedding & conference performances, mouth percussion classes, Indian mythology/ dance costume and make up workshops.
The final design should communicate a feeling and impression of the vibrance and energy of Indian dance.
Updates
Hi Everyone,
Project Deadline Extended
Reason: I would like to refine a few changes to the details of this lovely design and we have run out of time!
Project Deadline Extended
Reason: Still waiting to hear back form designer re two possible changes to the card design. Tomorrow is the deadline and I have sent several messages but with no response. I need to see this through before selecting this lovely design.
Thank you.
Tara
Industry/Entity Type
Preschool
Requirements
Must have
- The front of the business card should have the photo of me (my face and torso), surrounded entirely by a border of bright magenta (to match the magenta of my lipstick - it is the same as the magenta on my skirt in the second photo). Within the top border I want (perhaps yellow-gold) writing to say "Tara Holloway - Artistic Director" and within the bottom border it should read "Silver Creek Kathak Studio." If you turn the card on its side the left border should have my telephone number: 0417 826 394 and the right-hand border should read: silvercreekkathakstudio@fernmail.example
The reverse of the card should be the orange of the dance costume
and I'd like the picture of my feet and legs to be on the right side of the back of the card as a side border. Centre-aligned on the orange background it should read (perhaps in dark magenta):
Indian dance classes + private tuition
School + preschool educational courses and workshops
Dance theatre performances
Community function workshops and performances
Children's Bollywood parties
Wedding + conference performances
Mouth percussion classes
Indian mythology and dance demonstration workshops
Dance costume and make-up workshops
Nice to have
- A lovely artistic but easy-to-read font would be nice.

```html
<!DOCTYPE html>
<html lang="en">
<head>
<meta charset="UTF-8">
<title>Tara Holloway – Business Card</title>
<link href="https://fonts.googleapis.com/css2?family=Lobster&family=Lobster+Two&display=swap" rel="stylesheet">
<style>
  :root {
    --page: #ffffff;
    --magenta: #9c2951;
    --gold: #f2a334;
    --orange: #e07b2f;
    --white: #ffffff;
    --costume-magenta: #a0236e;
    --costume-gold: #e9a64a;
  }
  html, body {
    margin: 0;
    padding: 0;
    width: 1200px;
    height: 900px;
    overflow: hidden;
    background: var(--page);
  }
  .canvas {
    position: relative;
    width: 1200px;
    height: 900px;
  }
  .card {
    position: absolute;
    top: 131px;
    width: 387px;
    height: 632px;
    overflow: hidden;
  }
  .card-front {
    left: 163px;
    background: var(--magenta);
  }
  .card-back {
    left: 621px;
    background: var(--orange);
  }
  .headline {
    position: absolute;
    margin: 0;
    font-family: "Lobster", cursive;
    font-weight: 400;
    color: var(--gold);
    white-space: nowrap;
    line-height: 1;
  }
  .headline-name {
    left: 15px;
    top: 168px;
    font-size: 58px;
  }
  .headline-title {
    left: 9px;
    top: 245px;
    font-size: 60px;
  }
  .contact {
    position: absolute;
    margin: 0;
    font-family: "Lobster Two", cursive;
    color: var(--white);
    white-space: nowrap;
    line-height: 1;
  }
  .contact-email {
    left: 11px;
    top: 325px;
    font-size: 19.5px;
  }
  .contact-phone {
    right: 9px;
    top: 354px;
    font-size: 25px;
  }
  .portrait {
    position: absolute;
    left: 18px;
    top: 390px;
    width: 345px;
    height: 242px;
    border-radius: 46% 46% 0 0 / 40% 40% 0 0;
    background: radial-gradient(ellipse at 50% 30%, #e7c6b4 0 18%, #e3a53a 32%, #7d1c3e 75%);
  }
  .legs-photo {
    position: absolute;
    right: 0;
    top: 0;
    width: 267px;
    height: 632px;
    background: linear-gradient(100deg, rgba(224,123,47,0) 0%, var(--costume-magenta) 30%, #c01f74 50%, var(--costume-gold) 68%, #b8862f 80%, rgba(224,123,47,0.6) 100%);
  }
  .services {
    position: absolute;
    left: 11px;
    top: 0;
    margin: 0;
    padding: 0;
    list-style: none;
    font-family: "Lobster Two", cursive;
    font-size: 13.5px;
    line-height: 18px;
    color: var(--white);
  }
  .services li {
    position: absolute;
    left: 0;
    white-space: nowrap;
  }
</style>
</head>
<body>
  <main class="canvas">
    <section class="card card-front" aria-label="Card front">
      <h1 class="headline headline-name">Tara Holloway</h1>
      <h2 class="headline headline-title">Artistic Director</h2>
      <p class="contact contact-email">silvercreekkathakstudio@fernmail.example</p>
      <p class="contact contact-phone">0417 826 394</p>
      <div class="portrait" role="img" aria-label="Photo of Tara in classical Indian dance costume, hands raised beside her head"></div>
    </section>

    <section class="card card-back" aria-label="Card back">
      <div class="legs-photo" role="img" aria-label="Photo of a dancer's legs and feet in a magenta and gold silk costume with ankle bells"></div>
      <ul class="services">
        <li style="top:199px">Indian dance classes +<br>private tuition</li>
        <li style="top:253px">School +<br>preschool educational<br>courses and workshops</li>
        <li style="top:325px">Dance theatre performances</li>
        <li style="top:360px">Community function<br>workshops and performances</li>
        <li style="top:414px">Children's Bollywood parties</li>
        <li style="top:450px">Wedding + conference performances</li>
        <li style="top:486px">Mouth percussion classes</li>
        <li style="top:521px">Indian mythology and<br>dance demonstration workshop</li>
        <li style="top:575px">Dance costume and make-up workshops</li>
      </ul>
    </section>
  </main>
</body>
</html>
```